UPDATED 7/7 - Start-up Swimming Pool Care/Service Company In Need of Website

We sincerely appreciate everyone's interest in our website design project. In all we had 65 designs submitted and were amazed by the creativity and quality presented. Unfortunately, as with all contests, there can only be one winner and the winning firm was selected at 12:00 ET 7/7/2017. We wish you all the best and look forward to potentially working with you on future projects. Thanks again for your time and interests. Tobin

Thanks for your interest in our project! Due to the overwhelming number of submissions received, additional submissions will not be accepted after close of business 7/4. Additionally, to minimize unnecessary additional work, we will begin reviewing all submissions received on 7/5, select the submission(s) that come closest to meeting our needs and work with the designer(s) selected to finalize their designs. Thanks again.

Thanks for the feedback!!

Based on feedback provided, we understand that the initial specifications required that the site be developed as dynamic versus static and, as such, the budget was insufficient. With this in mind, we have modified the specifications as follows:
1. Clean, simple, uncluttered site
2. 4-5 pages consisting of the following:
a. Home page
b. About us
c. Services provided
d. Contact us/request quote/request service
2. No people in pools/photos unless it involves cleaning i.e., vacuuming, netting, etc.

We are in need of a website to promote our business and the services provided to our customers. The site should be a simple 5 page design providing information about us, the services we provide, our service territory (Central Florida = Seminole and Orange Counties), the ability to request a service quote, the ability to schedule service, the ability to pay invoices, the ability to refer neighbors and friends, the ability to leave reviews and provide feedback, etc. We are a certified, licensed, and insured veteran minority owned and operated company with 10 years industry experience providing unparalleled commercial and residential pool and spa care in the central Florida area. While we are seeking something more impressive and concise, an example of the site would be http://bluekettlepoolcare.example/ OR http://www.marlowaquaworks.example/

Target Market(s)

Hotels, motels, apartment complexes, condominium associations, homeowners associations, and individual homeowners

Contact Information for Business Card

Logo, name, phone number, website, "Certified Licensed Insured", "Providing quality pool care to Central Florida"

Coding

Coded - Design and coding required

Number of Pages Required

5+ page

Requirements
Must have
• See description
Nice to have
• See description
Should not have
• See description

```html
<!DOCTYPE html>
<html lang="en">
<head>
<meta charset="utf-8">
<title>Sunbelt Pool Care Co</title>
<link href="https://fonts.googleapis.com/css2?family=Montserrat:wght@400;500;600&family=Open+Sans:wght@400;600&display=swap" rel="stylesheet">
<style>
:root{
  --blue:#2a63a0;
  --blue-dark:#245890;
  --orange:#f3722a;
  --orange-soft:#f0904a;
  --ink:#555;
  --nav:#444;
  --grey-band:#efefef;
  --field-line:#cfcfcf;
  --white:#fff;
}
*{box-sizing:border-box;margin:0;padding:0}
html,body{width:697px;height:1200px;overflow:hidden;background:var(--white)}
body{position:relative;font-family:"Open Sans",Arial,sans-serif;color:var(--ink)}
.site-header{position:absolute;left:0;top:0;width:697px;height:85px}
.brand{position:absolute;left:45px;top:22px;font-family:"Montserrat",Arial,sans-serif;font-weight:600;font-size:20px;color:var(--blue);letter-spacing:.5px;display:flex;align-items:center;gap:8px}
.brand-dot{width:14px;height:14px;border-radius:50%;background:var(--orange);flex:none}
.top-contact{position:absolute;right:48px;top:13px;display:flex;gap:22px;font-family:"Montserrat",Arial,sans-serif;font-size:11px;color:var(--orange)}
.top-contact span{display:flex;align-items:center;gap:6px}
.main-nav{position:absolute;right:47px;top:47px;display:flex;gap:27px;font-family:"Montserrat",Arial,sans-serif;font-size:11px;color:var(--nav)}
.main-nav .active{color:var(--orange);position:relative}
.main-nav .active svg{position:absolute;left:0;top:14px}
.hero{position:absolute;left:0;top:85px;width:697px;height:360px}
.hero-photo{position:absolute;inset:0;background:linear-gradient(180deg,#4f86c6 0%,#a9c9e6 40%,#dfeaf3 55%,#3fa6da 70%,#2b8fd0 100%)}
.hero svg{position:absolute;left:0;bottom:0}
.welcome{position:absolute;top:463px;left:0;width:697px;text-align:center}
.welcome h1{font-family:"Montserrat",Arial,sans-serif;font-weight:400;font-size:23px;color:var(--blue);letter-spacing:.3px}
.welcome h1 em{font-style:normal;color:var(--orange)}
.welcome p{width:530px;margin:9px auto 0;font-size:9.3px;line-height:16px}
.services{position:absolute;top:570px;left:45px;display:flex;gap:21px}
.service{width:188px;text-align:center;position:relative}
.service-photo{height:102px}
.photo-net{background:linear-gradient(160deg,#5ed0f0,#1a8fd2 60%,#0f6fc0)}
.photo-yard{background:linear-gradient(180deg,#3d6b2e 0%,#6e9a4e 35%,#bfe4ee 60%,#7fcbe4 100%)}
.photo-spa{background:linear-gradient(180deg,#1aa6e8 0%,#48b8e6 35%,#b89a78 55%,#2d7fcf 80%,#9b7c60 100%)}
.service-icon{width:48px;height:48px;border-radius:50%;background:var(--orange);margin:-24px auto 0;position:relative;display:flex;align-items:center;justify-content:center}
.service h2{font-family:"Montserrat",Arial,sans-serif;font-weight:400;font-size:13.3px;line-height:19px;color:var(--blue);margin:8px -8px 0}
.service p{font-size:9.3px;line-height:16px;margin-top:5px;padding:0 4px}
.quote{position:absolute;top:826px;left:0;width:697px;height:260px;background:var(--grey-band)}
.quote h2{text-align:center;margin-top:27px;font-family:"Montserrat",Arial,sans-serif;font-weight:400;font-size:22px;color:var(--blue)}
.quote h2 em{font-style:normal;color:var(--orange)}
.field{position:absolute;background:var(--white);border:1px solid var(--field-line);font-size:9.3px;color:#666;padding:8px 8px}
.send{position:absolute;left:306px;top:187px;width:85px;height:30px;border-radius:15px;background:var(--orange);color:var(--white);font-family:"Montserrat",Arial,sans-serif;font-size:12px;text-align:center;line-height:30px;letter-spacing:.5px}
.footer-wave{position:absolute;left:0;top:1030px}
.site-footer{position:absolute;left:0;top:1088px;width:697px;height:112px;background:var(--blue);color:var(--white)}
.footer-brand{position:absolute;left:50px;top:18px;width:180px;font-family:"Montserrat",Arial,sans-serif;font-weight:600;font-size:17px;line-height:21px;display:flex;align-items:center;gap:8px}
.footer-brand .brand-dot{background:var(--white)}
.footer-col{position:absolute;top:15px}
.footer-col h3{font-family:"Montserrat",Arial,sans-serif;font-weight:400;font-size:11.5px;margin-bottom:7px}
.footer-col li{list-style:none;font-size:9.3px;display:flex;align-items:center;gap:7px;margin-bottom:6px}
.social{display:flex;gap:10px;margin-top:2px}
.social span{width:27px;height:27px;border-radius:50%;background:var(--white)}
.social span:first-child{background:var(--orange)}
.footer-rule{position:absolute;left:45px;top:83px;width:608px;height:1px;background:rgba(255,255,255,.2)}
.copyright{position:absolute;top:90px;width:697px;text-align:center;font-size:9.3px}
</style>
</head>
<body>
<header class="site-header">
  <div class="brand"><span class="brand-dot"></span>Sunbelt Pool Care Co</div>
  <div class="top-contact">
    <span><svg width="11" height="11" viewBox="0 0 24 24"><path fill="#2a63a0" d="M6.6 10.8c1.4 2.8 3.8 5.1 6.6 6.6l2.2-2.2c.3-.3.7-.4 1-.2 1.1.4 2.3.6 3.6.6.6 0 1 .4 1 1V20c0 .6-.4 1-1 1C10.6 21 3 13.4 3 4c0-.6.4-1 1-1h3.5c.6 0 1 .4 1 1 0 1.3.2 2.5.6 3.6.1.3 0 .7-.2 1z"/></svg>407.555.0142</span>
    <span><svg width="13" height="10" viewBox="0 0 26 20"><rect width="26" height="20" rx="2" fill="#2a63a0"/><path d="M1 2l12 9 12-9" stroke="#fff" stroke-width="2" fill="none"/></svg>support@sunbeltpoolcare.example</span>
  </div>
  <nav class="main-nav">
    <span class="active">HOME<svg width="34" height="6" viewBox="0 0 34 6"><path d="M0 4C10 0 22 0 34 4" stroke="#2a63a0" stroke-width="2" fill="none"/></svg></span>
    <span>ABOUT</span><span>SERVICES</span><span>CONTACT</span>
  </nav>
</header>

<section class="hero">
  <div class="hero-photo" role="img" aria-label="Sunlit infinity swimming pool with steel ladder under a blue sky"></div>
  <svg width="697" height="80" viewBox="0 0 697 80">
    <path d="M0 28C90 -2 180 10 290 42C380 68 470 60 560 40C620 26 660 14 697 0V80H0Z" fill="#e56a25"/>
    <path d="M0 38C90 12 190 22 290 50C380 74 480 66 560 46C620 32 665 20 697 10V80H0Z" fill="#fff"/>
  </svg>
</section>

<section class="welcome">
  <h1>WELCOME TO <em>SUNBELT POOL CARE CO</em></h1>
  <p>Lorem Ipsum is simply dummy text of the printing and typesetting industry. Lorem Ipsum has been the industry's standard dummy text ever since the 1500s, when an unknown printer took a galley of type and scrambled it to make a type specimen book.</p>
</section>

<section class="services">
  <article class="service">
    <div class="service-photo photo-net" role="img" aria-label="Hand skimming a pool surface with a leaf net"></div>
    <div class="service-icon"><svg width="24" height="24" viewBox="0 0 24 24" stroke="#fff" stroke-width="2.4" stroke-linecap="round"><path d="M5 5l14 14M19 5L5 19"/></svg></div>
    <h2>Pool Services &amp; Maintenance Plans</h2>
    <p>Lorem Ipsum is simply dummy text of the printing and typesetting industry. Lorem Ipsum has been the industry...</p>
  </article>
  <article class="service">
    <div class="service-photo photo-yard" role="img" aria-label="Residential backyard pool with lounge chairs and garden"></div>
    <div class="service-icon"><svg width="24" height="24" viewBox="0 0 24 24" stroke="#fff" stroke-width="2" fill="none" stroke-linecap="round"><path d="M8 3v14M15 3v14M8 8h7M8 13h7M3 20c3-2 6 2 9 0s6 2 9 0"/></svg></div>
    <h2>Commercial and Residential Pool Service</h2>
    <p>Lorem Ipsum is simply dummy text of the printing and typesetting industry. Lorem Ipsum has been the industry...</p>
  </article>
  <article class="service">
    <div class="service-photo photo-spa" role="img" aria-label="Round bubbling spa beside a custom pool deck"></div>
    <div class="service-icon"><svg width="24" height="24" viewBox="0 0 24 24" fill="#fff"><circle cx="7" cy="10" r="2"/><circle cx="12" cy="8" r="2"/><circle cx="17" cy="10" r="2"/><rect x="3" y="14" width="18" height="4" rx="2"/></svg></div>
    <h2>Custom Design pools and spa</h2>
    <p>Lorem Ipsum is simply dummy text of the printing and typesetting industry. Lorem Ipsum has been the industry...</p>
  </article>
</section>

<section class="quote">
  <h2>REQUEST A <em>FREE QUOTE</em></h2>
  <div class="field" style="left:110px;top:70px;width:175px;height:27px">Enter name</div>
  <div class="field" style="left:297px;top:70px;width:176px;height:27px">Enter email</div>
  <div class="field" style="left:484px;top:70px;width:176px;height:27px">Enter contact no.</div>
  <div class="field" style="left:110px;top:109px;width:550px;height:67px">Enter message</div>
  <div class="send">SEND</div>
</section>

<svg class="footer-wave" width="697" height="60" viewBox="0 0 697 60">
  <path d="M0 40C60 20 130 6 220 14C300 22 360 42 450 42C560 42 630 20 697 0V60H0Z" fill="#f0904a"/>
  <path d="M0 46C60 28 130 16 220 24C300 32 360 54 450 54C560 54 630 32 697 10V60H0Z" fill="#2a63a0"/>
</svg>

<footer class="site-footer">
  <div class="footer-brand"><span class="brand-dot"></span><span>Sunbelt Pool<br>Care Co</span></div>
  <div class="footer-col" style="left:256px">
    <h3>CONTACT INFO</h3>
    <ul>
      <li><svg width="10" height="10" viewBox="0 0 24 24"><path fill="#fff" d="M6.6 10.8c1.4 2.8 3.8 5.1 6.6 6.6l2.2-2.2c.3-.3.7-.4 1-.2 1.1.4 2.3.6 3.6.6.6 0 1 .4 1 1V20c0 .6-.4 1-1 1C10.6 21 3 13.4 3 4c0-.6.4-1 1-1h3.5c.6 0 1 .4 1 1 0 1.3.2 2.5.6 3.6.1.3 0 .7-.2 1z"/></svg>407.555.0142</li>
      <li><svg width="12" height="9" viewBox="0 0 26 20"><rect width="26" height="20" rx="2" fill="#fff"/><path d="M1 2l12 9 12-9" stroke="#2a63a0" stroke-width="2" fill="none"/></svg>support@sunbeltpoolcare.example</li>
    </ul>
  </div>
  <div class="footer-col" style="left:466px">
    <h3>FOLLOW US</h3>
    <div class="social"><span></span><span></span><span></span><span></span><span></span></div>
  </div>
  <div class="footer-rule"></div>
  <p class="copyright">© Sunbelt Pool Care Co - 2017. All Rights Reserved.</p>
</footer>
</body>
</html>
```